PSD website for property company

Please read the brief thoroughly.

We are looking for a new website for a property group that does property acquisitions, property development and property management.
They buy, build and lease core inner city industrial assets in Sydney, Australia.
They also invest in residential developments.

Site menu
- Home page
- Property – sub menus include – Leasing ; Projects ; Investments ; Property Management
- Capital and finance
- About
- Contact

They like this website
https://www.verlo.com.au/

They want the site to be clean, modern and bold.
They like few colors, even black and white is OK to submit

They have a logo and style guide and useable images here:
http://www.kumet.net/temp/PelorisWeb2019.zip
The zip file is also attached to this project.
We have supplied some images to give you an idea, but we will also require you to provide at least 3 extra images from stock photos.
Use your imagination.

I am expecting a lot of similar designs, so be aware the photos you choose will be really important.
They want really 3 good stock photos used and supplied without charge.
Please not too generic, I repeat the quality of the photos is important.
You may provide several photos (but not in multiple submissions please) and we will choose the best three to be provided.

The winner will be selected on a single home page design and required to provide;
All photos use in original format without charge
A second ‘standard page’ template design based on the winning home page design

```html
<!DOCTYPE html>
<html lang="en">
<head>
<meta charset="utf-8">
<title>Peloris Property</title>
<link href="https://fonts.googleapis.com/css2?family=Arimo:wght@400;700&display=swap" rel="stylesheet">
<style>
:root{
  --green:#536a30;
  --green-text:#4d6a2c;
  --ink:#222;
  --muted:#7f9a73;
  --band:#f3f8ec;
  --dark:#2b2b2b;
  --tile:#f4f3ef;
  --footer:#8fa886;
  --white:#fff;
}
*{box-sizing:border-box;margin:0;padding:0}
html,body{width:1200px;height:2718px;overflow:hidden}
body{font-family:'Arimo',Arial,sans-serif;color:var(--ink);background:var(--white);position:relative}
.abs{position:absolute}
.topbar{left:0;top:0;width:1200px;height:30px;background:var(--green);color:#fff;font-size:9px}
.topbar .mail{left:250px;top:9px}
.topbar .phone{left:375px;top:9px}
.topbar .social{left:866px;top:9px;display:flex;gap:14px}
.topbar .social span{width:11px;height:11px;border-radius:50%;background:#fff;opacity:.9;display:block}
.nav{left:0;top:30px;width:1200px;height:52px;border-bottom:1px solid #e4e4e4;background:#fff}
.logo{left:240px;top:15px;font-size:21px;font-weight:700;letter-spacing:5px;color:#1c1c1c}
.menu{left:537px;top:22px;display:flex;font-size:10.5px;font-weight:700;color:#222}
.menu li{list-style:none;margin-right:28px}
.menu li.active{color:var(--green-text)}
.menu li.caret::after{content:" ▾";font-size:8px}
.hero{left:0;top:82px;width:1200px;height:577px;background:linear-gradient(180deg,#c8d6c9 0%,#b9c5b2 45%,#8e9478 75%,#9aa08a 100%)}
.hero h1{position:absolute;left:240px;top:205px;font-size:40px;line-height:45px;font-weight:700;color:#2a2a2a}
.hero p{position:absolute;left:240px;top:302px;font-size:11.5px;font-weight:700;color:#222;line-height:13px;width:360px}
.hero .arrow{position:absolute;top:280px}
h2.section{position:absolute;width:1200px;left:0;text-align:center;font-size:20px;font-weight:700}
.sale-card{width:190px}
.photo{display:block;width:100%}
.card-title{font-size:15.5px;font-weight:700;color:var(--green-text);margin-top:16px}
.price{font-size:11px;font-weight:700;margin-top:5px}
.beds{font-size:11px;color:var(--muted);margin-top:9px}
.desc{font-size:9.5px;line-height:12px;margin-top:8px}
.btn{display:inline-block;font-size:10px;color:#fff;padding:4px 10px;margin-top:14px}
.btn-green{background:var(--green)}
.btn-dark{background:#2a2a2a}
.band{left:0;top:1205px;width:1200px;height:481px;background:var(--band)}
.feat-card{width:136px}
.about-img{left:240px;top:1766px;width:301px;height:265px;border:2px solid #8fa886;padding:4px}
.about-img div{width:100%;height:100%;background:radial-gradient(circle at 50% 50%,#d8b9a0 0%,#e9d5c6 35%,#fff 70%)}
.about-text{left:581px;top:1760px;width:380px}
.about-text h3{font-size:19.5px;color:var(--green-text);font-weight:700;margin-bottom:10px}
.about-text p{font-size:12.5px;line-height:15px;margin-bottom:15px}
.stat{top:2085px;width:135px;height:143px;background:var(--tile);text-align:center;clip-path:polygon(0 0,92% 0,100% 7%,100% 100%,0 100%)}
.stat svg{margin-top:33px}
.stat .num{font-size:16px;color:#555;margin-top:10px}
.stat .lbl{font-size:7.5px;color:#888;letter-spacing:.8px;margin-top:6px}
.contact{left:0;top:2304px;width:1200px;height:186px;background:var(--dark)}
.contact h3{position:absolute;left:240px;top:33px;font-size:21px;color:#fff;font-weight:700}
.form{left:240px;top:2379px;width:720px;height:224px;background:#fff;box-shadow:0 1px 4px rgba(0,0,0,.25)}
.field{position:absolute;border:1px solid #d0d0d0;font-size:11px;color:#777;padding:13px 15px}
.submit{position:absolute;left:584px;top:175px;width:128px;height:34px;background:var(--green);color:#fff;font-size:11px;font-weight:700;text-align:center;line-height:34px}
.footer{left:0;top:2674px;width:1200px;height:44px;background:var(--footer);color:#fff;text-align:center;font-size:15px;line-height:44px}
</style>
</head>
<body>
<header>
  <div class="abs topbar">
    <div class="abs mail">✉ hello@pelorisproperty.au</div>
    <div class="abs phone">☏ 123-456-7890</div>
    <div class="abs social"><span></span><span></span><span></span><span></span></div>
  </div>
  <nav class="abs nav">
    <div class="abs logo">PELORIS</div>
    <ul class="abs menu">
      <li class="active">HOME</li><li class="caret">PROPERTY</li><li class="caret">CAPITAL AND FINANCE</li><li class="caret">ABOUT</li><li class="caret" style="margin-left:10px">CONTACT</li>
    </ul>
  </nav>
</header>

<section class="abs hero" role="img" aria-label="Modern brick apartment building with arched windows and tree-lined street">
  <h1>WELCOME TO<br>PELORIS PROPERTY</h1>
  <p>Lorem ipsum dolor sit amet, consectetur adipiscing elit, sed do eiusmod tempor incididunt ut labore et dolore magna aliqua</p>
  <svg class="arrow" style="left:55px" width="14" height="16" viewBox="0 0 14 16"><path d="M11 1 3 8l8 7" fill="none" stroke="#222" stroke-width="3"/></svg>
  <svg class="arrow" style="left:1131px" width="14" height="16" viewBox="0 0 14 16"><path d="M3 1l8 7-8 7" fill="none" stroke="#222" stroke-width="3"/></svg>
</section>

<h2 class="section" style="top:714px;color:var(--green-text)">PROPERTIES FOR SALE</h2>
<article class="abs sale-card" style="left:240px;top:776px">
  <div class="photo" style="height:190px;background:linear-gradient(180deg,#8fb7e0 0%,#c9c3b5 45%,#5d9a3a 75%,#4e8a2e 100%)" role="img" aria-label="Two-storey beige family house with a lawn"></div>
  <div class="card-title">LOREM IPSUM</div><div class="price">$200,000</div><div class="beds">4 Bedrooms</div>
  <p class="desc">Lorem ipsum dolor sit amet, consectetur adipiscing elit, sed do eiusmod tempor incididunt ut labore et dolore magna aliqua. Ut enim ad minim veniam, quis nostrud exercitation ullamco laboris.</p>
  <span class="btn btn-green">READ MORE</span>
</article>
<article class="abs sale-card" style="left:504px;top:776px">
  <div class="photo" style="height:190px;background:linear-gradient(180deg,#c89a4a 0%,#e8e6e0 45%,#d9d5cc 75%,#8b8a50 100%)" role="img" aria-label="White cottage with red door and autumn tree"></div>
  <div class="card-title">LOREM IPSUM</div><div class="price">$100,000</div><div class="beds">3 Bedrooms</div>
  <p class="desc">Lorem ipsum dolor sit amet, consectetur adipiscing elit, sed do eiusmod tempor incididunt ut labore et dolore magna aliqua. Ut enim ad minim veniam, quis nostrud exercitation ullamco laboris.</p>
  <span class="btn btn-green">READ MORE</span>
</article>
<article class="abs sale-card" style="left:769px;top:770px">
  <div class="photo" style="height:190px;background:linear-gradient(180deg,#9cb9dc 0%,#c8d4e4 35%,#7a4a3e 55%,#4f8a30 85%)" role="img" aria-label="Large red brick colonial house with green lawn"></div>
  <div class="card-title">LOREM IPSUM</div><div class="price">$750,000</div><div class="beds">6 Bedrooms</div>
  <p class="desc">Lorem ipsum dolor sit amet, consectetur adipiscing elit, sed do eiusmod tempor incididunt ut labore et dolore magna aliqua. Ut enim ad minim veniam, quis nostrud exercitation ullamco laboris.</p>
  <span class="btn btn-green">READ MORE</span>
</article>

<section class="abs band"></section>
<h2 class="section" style="top:1264px;color:#222">FEATURE PROPERTIES</h2>
<article class="abs feat-card" style="left:240px;top:1325px">
  <div class="photo" style="height:135px;background:linear-gradient(180deg,#f1ece4 0%,#e0d6c6 55%,#bfb29c 100%)" role="img" aria-label="Bright living room with armchairs"></div>
  <div class="card-title" style="margin-top:21px">LOREM IPSUM</div>
  <p class="desc" style="margin-top:5px">Lorem ipsum dolor sit amet, consectetur adipiscing elit, sed do eiusmod tempor incididunt labore et dolore magna aliqua.</p>
  <span class="btn btn-dark" style="margin-top:12px">READ MORE</span>
</article>
<article class="abs feat-card" style="left:435px;top:1325px">
  <div class="photo" style="height:135px;background:linear-gradient(180deg,#7d6e60 0%,#a78b6e 45%,#9a4a25 100%)" role="img" aria-label="Dining room with wooden table and floors"></div>
  <div class="card-title" style="margin-top:21px">LOREM IPSUM</div>
  <p class="desc" style="margin-top:5px">Lorem ipsum dolor sit amet, consectetur adipiscing elit, sed do eiusmod tempor incididunt labore et dolore magna aliqua.</p>
  <span class="btn btn-dark" style="margin-top:12px">READ MORE</span>
</article>
<article class="abs feat-card" style="left:629px;top:1325px">
  <div class="photo" style="height:135px;background:linear-gradient(180deg,#eeeae4 0%,#b7a48a 50%,#6d5a48 100%)" role="img" aria-label="Open living room with sofa and coffee table"></div>
  <div class="card-title" style="margin-top:21px">LOREM IPSUM</div>
  <p class="desc" style="margin-top:5px">Lorem ipsum dolor sit amet, consectetur adipiscing elit, sed do eiusmod tempor incididunt labore et dolore magna aliqua.</p>
  <span class="btn btn-dark" style="margin-top:12px">READ MORE</span>
</article>
<article class="abs feat-card" style="left:823px;top:1325px">
  <div class="photo" style="height:135px;background:linear-gradient(180deg,#5e5c5a 0%,#8a8580 45%,#cfc9c0 70%,#7a5236 100%)" role="img" aria-label="Bedroom with grey walls and patterned rug"></div>
  <div class="card-title" style="margin-top:21px">LOREM IPSUM</div>
  <p class="desc" style="margin-top:5px">Lorem ipsum dolor sit amet, consectetur adipiscing elit, sed do eiusmod tempor incididunt labore et dolore magna aliqua.</p>
  <span class="btn btn-dark" style="margin-top:12px">READ MORE</span>
</article>

<div class="abs about-img"><div role="img" aria-label="Hands holding a small model house"></div></div>
<div class="abs about-text">
  <h3>ABOUT PELORIS PROPERTY</h3>
  <p>Lorem ipsum dolor sit amet, consectetur adipiscing elit, sed do eiusmod tempor incididunt ut labore et dolore magna aliqua. Ut enim ad minim veniam, quis nostrud exercitation ullamco laboris nisi ut aliquip ex ea commodo consequat. Duis aute irure dolor in reprehenderit in voluptate velit esse cillum dolore eu fugiat nulla pariatur.</p>
  <p>consectetur adipiscing elit, sed do eiusmod tempor incididunt ut labore et dolore magna aliqua. Ut enim ad minim veniam, quis nostrud exercitation ullamco laboris nisi ut aliquip ex ea commodo consequat. Duis aute irure dolor in reprehenderit in voluptate velit.</p>
  <p>Sed ut perspiciatis unde omnis iste natus error sit voluptatem accusantium doloremque laudantium, totam rem aperiam, eaque ipsa quae ab illo inventore veritatis et quasi architecto beatae vitae dicta sunt explicabo.</p>
</div>

<div class="abs stat" style="left:240px">
  <svg width="32" height="32" viewBox="0 0 32 32" fill="none" stroke="#555" stroke-width="1.5"><path d="M4 28 28 4M4 4l24 24"/><rect x="2" y="24" width="6" height="6"/><rect x="24" y="2" width="6" height="6"/></svg>
  <div class="num">2450</div><div class="lbl">SQUARE FEET</div>
</div>
<div class="abs stat" style="left:386px">
  <svg width="32" height="32" viewBox="0 0 32 32" fill="none" stroke="#555" stroke-width="1.5"><rect x="4" y="6" width="24" height="10"/><rect x="2" y="16" width="28" height="8"/><path d="M4 24v4M28 24v4M8 10h6v6H8zM18 10h6v6h-6z"/></svg>
  <div class="num">6</div><div class="lbl">BEDROOMS</div>
</div>
<div class="abs stat" style="left:532px">
  <svg width="32" height="32" viewBox="0 0 32 32" fill="none" stroke="#555" stroke-width="1.5"><path d="M2 16h28v4a6 6 0 0 1-6 6H8a6 6 0 0 1-6-6zM6 16V5a3 3 0 0 1 6 0M8 26l-2 3M24 26l2 3"/></svg>
  <div class="num">4</div><div class="lbl">BEDROOMS</div>
</div>
<div class="abs stat" style="left:678px">
  <svg width="32" height="32" viewBox="0 0 32 32" fill="none" stroke="#555" stroke-width="1.5"><path d="M2 14 16 3l14 11M6 11v18h20V11"/><rect x="13" y="20" width="6" height="9"/><rect x="9" y="14" width="5" height="4"/><rect x="18" y="14" width="5" height="4"/></svg>
  <div class="num">2016</div><div class="lbl">YEAR BUILT</div>
</div>
<div class="abs stat" style="left:824px">
  <svg width="32" height="32" viewBox="0 0 32 32" fill="none" stroke="#555" stroke-width="1.5"><path d="M2 12 16 3l14 9v17H2z"/><path d="M7 14h18v15M7 14v15M7 18h18M7 22h18M7 26h18"/></svg>
  <div class="num">2</div><div class="lbl">CAR PARKING</div>
</div>

<section class="abs contact"><h3>CONTACT US</h3></section>
<form class="abs form">
  <div class="field" style="left:8px;top:8px;width:223px;height:40px">NAME</div>
  <div class="field" style="left:248px;top:8px;width:223px;height:40px">PHONE</div>
  <div class="field" style="left:489px;top:8px;width:223px;height:40px">EMAIL</div>
  <div class="field" style="left:8px;top:65px;width:704px;height:88px">MESSAGE</div>
  <div class="submit">SUBMIT</div>
</form>

<footer class="abs footer">© 2019 Peloris Property All Rights Reserved</footer>
</body>
</html>
```